LWTrendco

I ran out of business cards I designed myself on line. THe company went out of business and I LOVE my card. I am hoping someone can recreate the look or something equally as appealing to me.

Industry/Entity Type

Business

Colors
ecdaeb
f7f1f7

Requirements
Must have
• The card is going to be printed by a company Quibzo.com. they are very high end stock and I market to high end clients…the logo needs to remain small and centered at the top. If it helps my web site is lwtrendco.net you can see there how I left the logo very small

```html
<!DOCTYPE html>
<html lang="en">
<head>
<meta charset="utf-8">
<title>LWTrendco, LLC — Business Card</title>
<link rel="stylesheet" href="https://fonts.googleapis.com/css2?family=Crimson+Text:wght@400&display=swap">
<style>
  :root {
    --frame: #ecdaeb;
    --paper: #f7f1f7;
    --ink: #1a1a1a;
  }
  * { margin: 0; padding: 0; box-sizing: border-box; }
  html, body {
    width: 667px;
    height: 1200px;
    overflow: hidden;
    background: var(--frame);
  }
  .card {
    position: relative;
    width: 667px;
    height: 1200px;
    background: var(--frame);
    font-family: "Crimson Text", Georgia, serif;
    color: var(--ink);
  }
  .card__paper {
    position: absolute;
    inset: 18px;
    background: var(--paper);
  }
  .card__line {
    position: absolute;
    left: 0;
    width: 100%;
    text-align: center;
    line-height: 1;
    white-space: nowrap;
  }
  .brand-mark {
    top: 188px;
    font-size: 44px;
    letter-spacing: 0.02em;
  }
  .company-name {
    top: 472px;
    font-size: 57px;
    letter-spacing: 0.01em;
  }
  .tagline {
    top: 726px;
    font-size: 31px;
    letter-spacing: 0.01em;
  }
  .contact-name {
    top: 948px;
    font-size: 44px;
    font-variant: small-caps;
    letter-spacing: 0.01em;
  }
  .contact-phone {
    top: 1026px;
    font-size: 34px;
  }
  .contact-email {
    top: 1070px;
    font-size: 39px;
    letter-spacing: 0.01em;
  }
</style>
</head>
<body>
  <main class="card">
    <div class="card__paper"></div>
    <p class="card__line brand-mark">LWTrendco</p>
    <h1 class="card__line company-name" style="font-weight:400">LWTRENDCO, LLC</h1>
    <p class="card__line tagline">DESIGN &amp; RENOVATION</p>
    <p class="card__line contact-name">Marisol denhart</p>
    <p class="card__line contact-phone">410-555-0182</p>
    <p class="card__line contact-email">MARISOL@LWTRENDCO.NET</p>
  </main>
</body>
</html>
```